Kindred Stretch - Logo and Business card design

I require a business card design for my Yoga teaching business. I have a design for a logo I would like to use on the card. I would like the logo designed and provided to me separately to the business card in a jpg or tiff high resolution file so I can use this for a web site, letter head, banner in the future.
I am a travelling yoga teacher in Sydney and teach at several gyms, corporates, private clients, schools, yoga studios etc
With the design I have sent thru as a guide,I would like my own text and colours inside this logo. I have a very good idea of how I would like this to look the logo and business name on the front and contact details on the back.

Target Market(s)

Private clients, corporates, schools, gyms, studios, healthcare industry

Industry/Entity Type

Teacher

Requirements
Must have
• What is compulsory is the information sent in the uploaded file
This card must have a feel for the regular yogi to a beginner so that anyone can practice yoga and feel fantastic.
Nice to have
• refer to attached file
Should not have
• I really do not want this to be a boring Yoga card that does not relate to the average person.

```html
<!DOCTYPE html>
<html lang="en">
<head>
<meta charset="utf-8">
<title>Kindred Stretch – Business Card</title>
<link href="https://fonts.googleapis.com/css2?family=Ubuntu:wght@300;400&display=swap" rel="stylesheet">
<style>
  :root {
    --backdrop: #e9e7ea;
    --card: #f7f7f5;
    --card-edge: #dcdcda;
    --plum: #a0289c;
    --ink: #555558;
    --figure-violet: #8e3d9a;
    --figure-green: #9cc24a;
  }
  * { margin: 0; padding: 0; box-sizing: border-box; }
  html, body {
    width: 1200px;
    height: 883px;
    overflow: hidden;
    background: var(--backdrop);
    font-family: "Ubuntu", sans-serif;
  }
  .canvas {
    width: 1200px;
    height: 883px;
    display: flex;
    align-items: center;
    justify-content: center;
    gap: 60px;
  }
  .card {
    width: 520px;
    height: 318px;
    background: var(--card);
    border: 1px solid var(--card-edge);
    box-shadow: 0 6px 18px rgba(0, 0, 0, 0.12);
    position: relative;
    overflow: hidden;
  }
  .card-back {
    padding: 58px 0 0 56px;
    color: var(--ink);
  }
  .teacher-name {
    font-weight: 400;
    font-size: 50px;
    color: var(--plum);
    letter-spacing: 0.5px;
    line-height: 1;
  }
  .credential {
    font-weight: 400;
    font-size: 16px;
    margin-top: 16px;
  }
  .credential-secondary {
    font-size: 13px;
    margin-top: 6px;
  }
  .contact {
    margin-top: 34px;
    list-style: none;
    font-size: 15px;
    font-weight: 300;
    line-height: 1.9;
  }
  .contact-label { display: inline-block; width: 28px; font-weight: 400; }
  .card-front {
    display: flex;
    align-items: center;
    justify-content: center;
  }
  .meditation-figure {
    width: 250px;
    height: 200px;
    border-radius: 48% 48% 30% 30% / 40% 40% 26% 26%;
    background: radial-gradient(ellipse at 50% 45%, var(--figure-green) 0%, var(--figure-violet) 75%);
    opacity: 0.85;
  }
</style>
</head>
<body>
  <main class="canvas">
    <section class="card card-back">
      <h1 class="teacher-name">Mara Ellison</h1>
      <p class="credential">Certified Vinyasa Yoga Teacher</p>
      <p class="credential credential-secondary">Advanced Mind Body Flow Instructor</p>
      <ul class="contact">
        <li><span class="contact-label">M:</span>0412 555 308</li>
        <li><span class="contact-label">E:</span>hello@kindredstretch.com</li>
      </ul>
    </section>
    <section class="card card-front">
      <div class="meditation-figure" role="img" aria-label="Seated lotus-pose figure formed from a word cloud of yoga words such as Kindred Stretch, breathe, balance, focus and energy, in purple and green"></div>
    </section>
  </main>
</body>
</html>
```